Business Cards for Marco and Tobin

Design of business cards for two people with the recently created brand Valcor Mobile. Valcor Mobile wants to become a worldwide major player on the secondhand phone market. It gathers send hand phones from individuals, refurbish them and sell them throughout the world. It has a green impact (recycling) and we also contribute to social project in Africa (a percentage of our benefits are sent to build school, sport facilities, etc.

Target Market(s)

B2B - Marco and Tobin are in contact with distributors across Africa.

Industry/Entity Type

Wireless Communication

Contact Information for Business Card

Marco Feuillet
Head of Emerging Markets
Valcor Energy South Africa (Pty) Ltd
Kestrel Road 47
2031 Sandton - Johannesburg
South Africa
Tel: + 27 10 555 0148
Mobile : +27 82 55 104
Email : marco.feuillet@valcormobile.example
Skype: marco.feuillet
Web: www.valcormobile.example
 

Tobin Farrow
Head of Southern Africa
Kestrel Road 47
South Africa
Tel: + 27 10 555 0148
Mobile: +27 83 555 0276
Email: tobin.farrow@valcormobile.example
Skype: tobin.farrow
Web: www.valcormobile.example

Requirements
Must have
• The cards need to be "serious", trustable, with a worldwide presence.
Nice to have
• Some "green" / recycling touch would be nice but not necessary if in contradiction with the general design.

```html
<!DOCTYPE html>
<html lang="en">
<head>
<meta charset="utf-8">
<title>Valcor Mobile – Business Card</title>
<link rel="stylesheet" href="https://fonts.googleapis.com/css2?family=Open+Sans:wght@400;600;700&display=swap">
<style>
  :root {
    --backdrop: #bdbdbd;
    --card-white: #ffffff;
    --navy: #0d2a4a;
    --brand-blue: #2b93d6;
    --back-blue: #0f7fcc;
    --back-pattern: #2a8fd5;
    --text-grey: #444a50;
    --text-dark: #1c2a38;
  }
  * { box-sizing: border-box; margin: 0; padding: 0; }
  html, body { width: 1200px; height: 900px; overflow: hidden; }
  body {
    background: var(--backdrop);
    font-family: "Open Sans", Arial, sans-serif;
    position: relative;
  }
  .card {
    position: absolute;
    top: 306px;
    width: 441px;
    height: 271px;
    box-shadow: 2px 3px 5px rgba(0,0,0,0.35);
    overflow: hidden;
  }
  .card--front { left: 149px; background: var(--card-white); }
  .card--back { left: 608px; background: var(--back-blue); }

  .corner-accent { position: absolute; left: 0; top: 26px; }
  .holder { position: absolute; left: 35px; top: 28px; }
  .holder__name { font-size: 18.5px; font-weight: 700; color: var(--navy); line-height: 22px; }
  .holder__title { font-size: 12px; color: var(--text-grey); line-height: 16px; }

  .contact-list { position: absolute; left: 20px; top: 138px; list-style: none; }
  .contact-list li { font-size: 12px; color: var(--text-dark); line-height: 15.5px; display: flex; align-items: center; gap: 4px; }
  .contact-list svg { width: 10px; height: 10px; flex: none; }

  .company { position: absolute; left: 20px; top: 194px; font-size: 12px; line-height: 16px; color: var(--text-grey); }
  .company__name { font-weight: 700; color: var(--navy); }

  .brand-name {
    position: absolute; left: 258px; top: 142px;
    font-size: 23px; font-weight: 700; color: var(--navy); letter-spacing: -0.3px;
  }
  .online { position: absolute; right: 24px; top: 210px; text-align: right; list-style: none; }
  .online li { font-size: 12px; line-height: 16px; color: var(--text-dark); display: flex; justify-content: flex-end; align-items: center; gap: 4px; }
  .online svg { width: 11px; height: 11px; }

  .footer-band { position: absolute; left: 0; bottom: 0; }

  .back-pattern {
    position: absolute; left: 10px; top: 8px; right: 10px; bottom: 8px;
    background: var(--back-pattern); opacity: 0.55; border-radius: 4px;
  }
  .back-brand {
    position: absolute; left: 0; right: 0; top: 118px; text-align: center;
    font-size: 23px; font-weight: 700; color: #ffffff; letter-spacing: -0.3px;
  }
</style>
</head>
<body>

  <section class="card card--front" aria-label="Business card front">
    <svg class="corner-accent" width="30" height="38" viewBox="0 0 30 38">
      <polygon points="0,0 9,0 16,37 0,37" fill="var(--navy)"/>
      <polygon points="10,0 28,0 28,37 17,37" fill="var(--brand-blue)"/>
    </svg>

    <div class="holder">
      <p class="holder__name">Marco Feuillet</p>
      <p class="holder__title">Head of Emerging Markets</p>
    </div>

    <ul class="contact-list">
      <li>
        <svg viewBox="0 0 10 10"><path d="M1 3 Q5 0 9 3 L8 4.5 L6.5 3.8 L6.5 3 Q5 2.5 3.5 3 L3.5 3.8 L2 4.5 Z M2 5 H8 L9 9 H1 Z" fill="var(--navy)"/></svg>
        27 10 555 0148
      </li>
      <li>
        <svg viewBox="0 0 10 10"><rect x="2.5" y="0.5" width="5" height="9" rx="1" fill="none" stroke="var(--navy)" stroke-width="1.2"/><circle cx="5" cy="8" r="0.6" fill="var(--navy)"/></svg>
        +27 82 55 104
      </li>
      <li>
        <svg viewBox="0 0 10 10"><rect x="0.5" y="2" width="9" height="6" fill="var(--navy)"/><path d="M0.5 2 L5 5.5 L9.5 2" fill="none" stroke="#fff" stroke-width="0.9"/></svg>
        marco.feuillet@valcormobile.example
      </li>
    </ul>

    <div class="company">
      <p class="company__name">Valcor Energy South Africa (Pty) Ltd</p>
      <p>Kestrel Road 47 2031 Sandton</p>
      <p>Johannesburg South Africa</p>
    </div>

    <p class="brand-name">ValcorMobile</p>

    <ul class="online">
      <li>www.valcormobile.example
        <svg viewBox="0 0 12 12"><circle cx="6" cy="6" r="5.2" fill="var(--navy)"/><ellipse cx="6" cy="6" rx="2.2" ry="5.2" fill="none" stroke="#fff" stroke-width="0.8"/><line x1="0.8" y1="6" x2="11.2" y2="6" stroke="#fff" stroke-width="0.8"/></svg>
      </li>
      <li>marco.feuillet
        <svg viewBox="0 0 12 12"><circle cx="6" cy="6" r="5.5" fill="var(--navy)"/></svg>
      </li>
    </ul>

    <svg class="footer-band" width="441" height="20" viewBox="0 0 441 20">
      <polygon points="0,6 216,6 208,20 0,20" fill="var(--navy)"/>
      <polygon points="222,2 441,2 441,20 207,20" fill="var(--brand-blue)"/>
    </svg>
  </section>

  <section class="card card--back" aria-label="Business card back">
    <div class="back-pattern" role="img" aria-label="Repeating brand pattern in light blue across the card back"></div>
    <p class="back-brand">ValcorMobile</p>
  </section>

</body>
</html>
```